Political Candidate Newspaper Advertisement

I would like a newspaper ad for my campaign for election to City Council. The banner ad is 10 cm high x 26.2 cm wide. The banner will contain a photo and the following text (or words to similar effect):
VOTE
DENNIS HALE
COMO BEACH
For a
SAFE
CARING
CONNECTED
COMMUNITY
Lifetime commitment to local clubs, charities and international aid
Local business owner
Founder of Open-Gate Week
Councillor, Mediator, B.Sc., MBA
The Councillor you know and can call for help
Respects our heritage and our future
Listens to the wisdom and needs of older residents
Promotes more young people
Protects our South Perth environment
Authorised by Dennis Hale 5/348 Kelby Rd, Como. 9317 2864
I use MS Publisher and PhotoShop so I'd like the product to be in a form I can use. After ther banner ad is done, and if it is good, I wish to pay the designer to use the same theme to produce another newspaper ad, a brochure and a poster.
My simple version is attached. A photo is also attached.
I'm hoping you do better.
18-80 years old
Business
- simple fonts
- A TICK somewhere around the word Vote would be good.
Mention of www.fairlandward.notepage.net if possible, perhaps at the bottom of the page, along with the Authorised by ... text.

```html
<!DOCTYPE html>
<html lang="en">
<head>
<meta charset="utf-8">
<title>Vote Dennis Hale – Como Beach</title>
<link href="https://fonts.googleapis.com/css2?family=Barlow:wght@600;700;800&family=Barlow+Semi+Condensed:ital,wght@1,500&display=swap" rel="stylesheet">
<style>
  :root {
    --frame-green: #2fd62a;
    --frame-light: #8ef07f;
    --field-blue: #0b2fc2;
    --vote-red: #e40d12;
    --deep-red: #b0080c;
    --tick-green: #22c41a;
    --vote-yellow: #f6ea16;
    --white: #ffffff;
    --note-yellow: #f2e21c;
    --photo-green: #39e03a;
  }
  * { margin: 0; padding: 0; box-sizing: border-box; }
  html, body { width: 1200px; height: 601px; overflow: hidden; background: var(--white); }
  .canvas { position: relative; width: 1200px; height: 601px; font-family: "Barlow", Arial, sans-serif; }
  .shapes { position: absolute; inset: 0; }
  .vote {
    position: absolute; left: 108px; top: 112px; width: 270px; text-align: center;
    font-weight: 800; font-size: 46px; letter-spacing: 3px; line-height: 1;
    color: var(--vote-yellow);
    -webkit-text-stroke: 1.5px var(--deep-red);
    text-shadow: 2px 3px 0 var(--deep-red);
  }
  .candidate {
    position: absolute; left: 115px; top: 200px; width: 215px; text-align: center;
    font-weight: 700; font-size: 66px; line-height: 0.98; color: var(--vote-red);
    letter-spacing: -1px;
    text-shadow: 2px 3px 3px rgba(0,0,0,0.35);
  }
  .suburb {
    position: absolute; left: 170px; top: 370px; width: 122px; text-align: center;
    font-weight: 700; font-size: 25px; line-height: 1.05; color: var(--white);
    text-shadow: 1px 2px 2px rgba(0,0,0,0.45);
  }
  .slogan {
    position: absolute; right: 658px; top: 178px; text-align: right;
    font-weight: 700; color: var(--white); line-height: 1;
    text-shadow: 2px 3px 3px rgba(0,0,0,0.45);
  }
  .slogan .lead { display: block; font-size: 30px; margin-bottom: 14px; font-weight: 600; }
  .slogan .word { display: block; font-size: 35px; letter-spacing: 1px; margin-bottom: 13px; }
  .credentials { position: absolute; left: 612px; top: 124px; list-style: none; }
  .credentials li {
    position: absolute; left: 0; width: 300px; padding-left: 32px;
    font-weight: 700; font-size: 14.5px; line-height: 16px; color: var(--white);
  }
  .credentials li svg { position: absolute; left: 0; top: -4px; width: 27px; height: 27px; }
  .credentials small { font-size: 11px; }
  .authorisation {
    position: absolute; right: 116px; top: 461px;
    font-family: "Barlow Semi Condensed", Arial, sans-serif; font-style: italic; font-weight: 500;
    font-size: 11px; color: var(--note-yellow);
  }
</style>
</head>
<body>
<div class="canvas">
  <svg class="shapes" width="1200" height="601" viewBox="0 0 1200 601" aria-hidden="true">
    <defs>
      <clipPath id="field-clip"><rect x="82" y="104" width="1018" height="381"/></clipPath>
      <radialGradient id="red-ball" cx="40%" cy="35%" r="70%">
        <stop offset="0" stop-color="#f21a1e"/><stop offset="1" stop-color="#c9090d"/>
      </radialGradient>
      <linearGradient id="photo-tone" x1="0" y1="0" x2="0.8" y2="1">
        <stop offset="0" stop-color="var(--photo-green)"/><stop offset="0.45" stop-color="#e9f7e6"/><stop offset="1" stop-color="#ffffff"/>
      </linearGradient>
      <filter id="soft-shadow" x="-20%" y="-20%" width="140%" height="140%">
        <feDropShadow dx="3" dy="5" stdDeviation="5" flood-color="#000" flood-opacity="0.45"/>
      </filter>
      <symbol id="tick-mark" viewBox="0 0 100 100">
        <path d="M8 52 L30 40 L42 62 C56 34 74 16 96 6 C72 30 56 58 44 92 Z" fill="var(--tick-green)" stroke="var(--white)" stroke-width="4" stroke-linejoin="round"/>
      </symbol>
    </defs>
    <rect class="frame" x="75" y="97" width="1032" height="395" fill="var(--frame-green)"/>
    <rect x="78" y="100" width="1026" height="389" fill="none" stroke="var(--frame-light)" stroke-width="2"/>
    <rect class="field" x="82" y="104" width="1018" height="381" fill="var(--field-blue)"/>
    <g clip-path="url(#field-clip)">
      <path class="corner-swell" d="M82 104 H497 C488 220 400 300 250 322 C180 330 120 330 82 328 Z" fill="url(#red-ball)" filter="url(#soft-shadow)"/>
      <circle class="slogan-disc" cx="445" cy="318" r="150" fill="url(#red-ball)" filter="url(#soft-shadow)"/>
      <circle class="name-disc" cx="222" cy="262" r="107" fill="var(--white)" filter="url(#soft-shadow)"/>
      <circle class="suburb-disc" cx="231" cy="396" r="62" fill="url(#red-ball)" filter="url(#soft-shadow)"/>
      <circle class="portrait" cx="988" cy="266" r="126" fill="url(#photo-tone)" role="img" aria-label="Portrait photo of the candidate smiling in a suit and tie"/>
    </g>
    <use href="#tick-mark" x="326" y="118" width="118" height="118" filter="url(#soft-shadow)"/>
  </svg>

  <div class="vote">VOTE</div>
  <div class="candidate">Dennis<br>Hale</div>
  <div class="suburb">COMO<br>BEACH</div>
  <div class="slogan">
    <span class="lead">For a</span>
    <span class="word">SAFE</span>
    <span class="word">CARING</span>
    <span class="word">CONNECTED</span>
    <span class="word">COMMUNITY</span>
  </div>

  <ul class="credentials">
    <li style="top:6px"><svg viewBox="0 0 100 100"><circle cx="50" cy="50" r="46" fill="var(--white)"/><use href="#tick-mark" x="8" y="4" width="90" height="90"/></svg>Lifetime commitment to local clubs, charities and international aid</li>
    <li style="top:52px"><svg viewBox="0 0 100 100"><circle cx="50" cy="50" r="46" fill="var(--white)"/><use href="#tick-mark" x="8" y="4" width="90" height="90"/></svg>Local business owner</li>
    <li style="top:82px"><svg viewBox="0 0 100 100"><circle cx="50" cy="50" r="46" fill="var(--white)"/><use href="#tick-mark" x="8" y="4" width="90" height="90"/></svg>Founder of Open-Gate Week</li>
    <li style="top:113px"><svg viewBox="0 0 100 100"><circle cx="50" cy="50" r="46" fill="var(--white)"/><use href="#tick-mark" x="8" y="4" width="90" height="90"/></svg>Councillor, Mediator, <small>B.Sc., MBA</small></li>
    <li style="top:144px"><svg viewBox="0 0 100 100"><circle cx="50" cy="50" r="46" fill="var(--white)"/><use href="#tick-mark" x="8" y="4" width="90" height="90"/></svg>The Councillor you know and<br>can call for help</li>
    <li style="top:190px"><svg viewBox="0 0 100 100"><circle cx="50" cy="50" r="46" fill="var(--white)"/><use href="#tick-mark" x="8" y="4" width="90" height="90"/></svg>Respects our heritage and<br>our future</li>
    <li style="top:236px"><svg viewBox="0 0 100 100"><circle cx="50" cy="50" r="46" fill="var(--white)"/><use href="#tick-mark" x="8" y="4" width="90" height="90"/></svg>Listens to the wisdom and needs<br>of older residents</li>
    <li style="top:281px"><svg viewBox="0 0 100 100"><circle cx="50" cy="50" r="46" fill="var(--white)"/><use href="#tick-mark" x="8" y="4" width="90" height="90"/></svg>Promotes more young people</li>
    <li style="top:311px"><svg viewBox="0 0 100 100"><circle cx="50" cy="50" r="46" fill="var(--white)"/><use href="#tick-mark" x="8" y="4" width="90" height="90"/></svg>Protects our South Perth environment</li>
  </ul>

  <p class="authorisation">Authorised by Dennis Hale 5/348 Kelby Rd, Como. 9317 2864</p>
</div>
</body>
</html>
```